Business Card Design

I am a Building Surveyor and run my own Building Consultat company, providing professional advice and services to builders, architects, designers, owners, etc.

Industry/Entity Type

Business

Contact Information for Business Card

Dorwen Fasque BBldgSurv (Hons)
Managing Director

47 Marlow Crest, Kelvoth Downs WA 6158
Mobile 0498 153 607
Email Dorwen.fasque@ridgeplumbav.com

Requirements
Must have
• I would like the back of the business card to be one colour (a shade of either black or maroon, matching the colours of my logo). Positioned in the centre on the back of the business card is to be my logo.

The front of the card is to be white, with my contact information in either black or maroon. The ADBldgSurv after my name should be in a smaller font size than my name. I would also like a small logo somewhere on this side of the card.

```html
<!DOCTYPE html>
<html lang="en">
<head>
<meta charset="utf-8">
<title>Kelvoth Building Advisory – Business Card</title>
<link rel="stylesheet" href="https://fonts.googleapis.com/css2?family=EB+Garamond:wght@400;500&display=swap">
<style>
  :root {
    --maroon: #67261d;
    --white: #ffffff;
    --charcoal: #4a4a4a;
    --rule-grey: #5a5a5a;
    --silver: #b3aaa7;
    --page: #ffffff;
    --card-edge: #9a9a9a;
  }
  * { margin: 0; padding: 0; box-sizing: border-box; }
  html, body {
    width: 984px;
    height: 1200px;
    overflow: hidden;
    background: var(--page);
    font-family: "EB Garamond", Garamond, serif;
  }
  .sheet { position: relative; width: 984px; height: 1200px; }

  .card { position: absolute; left: 55px; width: 882px; height: 533px; overflow: hidden; }
  .card--front { top: 39px; border: 1px solid var(--card-edge); background: var(--white); }
  .card--back { top: 599px; background: var(--maroon); }

  /* front: brand band */
  .brand-band { position: absolute; left: 0; top: 0; width: 100%; height: 222px; }
  .brand-band__mark { position: absolute; left: 75px; top: 66px; }
  .brand-band__name {
    position: absolute; left: 252px; top: 72px;
    font-size: 52px; font-weight: 500; color: var(--charcoal);
    letter-spacing: 1px; line-height: 1.15;
  }
  .band-rule { position: absolute; left: 0; top: 222px; width: 100%; height: 5px; background: var(--rule-grey); }

  /* front: contact panel */
  .contact-panel {
    position: absolute; left: 0; top: 229px; width: 100%; height: 304px;
    background: var(--maroon); color: var(--white);
  }
  .holder { position: absolute; left: 71px; top: 40px; }
  .holder__name { font-size: 40px; font-weight: 400; line-height: 1.1; }
  .holder__title { font-size: 21px; margin-top: 4px; }
  .details {
    position: absolute; right: 68px; top: 76px;
    text-align: right; font-size: 26px; line-height: 38px;
    list-style: none;
  }

  /* back */
  .back-mark { position: absolute; left: 352px; top: 118px; }
  .back-name {
    position: absolute; left: 0; top: 336px; width: 100%;
    text-align: center; font-size: 46px; font-weight: 500;
    color: var(--silver); letter-spacing: 1px;
  }
</style>
</head>
<body>
<main class="sheet">

  <section class="card card--front" aria-label="Business card front">
    <header class="brand-band">
      <svg class="brand-band__mark" width="112" height="112" viewBox="0 0 112 112" aria-hidden="true">
        <circle cx="56" cy="56" r="54" fill="var(--maroon)"/>
      </svg>
      <p class="brand-band__name">KELVOTH BUILDING<br>ADVISORY</p>
    </header>
    <div class="band-rule"></div>
    <div class="contact-panel">
      <div class="holder">
        <h1 class="holder__name">Dorwen Fasque</h1>
        <p class="holder__title">ADBldg Surv DIRECTOR</p>
      </div>
      <ul class="details">
        <li>47 Marlow Crest,</li>
        <li>Kelvoth Downs WA 6158</li>
        <li>Mobile 0498 153 607</li>
        <li>Dorwen.fasque@ridgeplumbav.com</li>
      </ul>
    </div>
  </section>

  <section class="card card--back" aria-label="Business card back">
    <svg class="back-mark" width="176" height="176" viewBox="0 0 176 176" aria-hidden="true">
      <circle cx="88" cy="88" r="86" fill="var(--silver)"/>
    </svg>
    <p class="back-name">KELVOTH BUILDING ADVISORY</p>
  </section>

</main>
</body>
</html>
```